Women's Shelter Website Design

We are working with a Women's Shelter in California. They provide services and shelter for women and mothers throughout California.
Some sites to use for inspiration:
https://harborlightcommons.org
https://qbrtl.org
https://www.kemjy.org
https://plmfarrowby.org
https://www.gvhollow.org (I love the banner, navigation and upper navigation)
https://bellmereroost.org (love the idea of an EXIT NOW button)
Thank you for taking the time to consider designing a website for us. We are web developers based in Stockton, CA, USA. Most of our projects go through the same process. Understanding this process may help you win a project with us. We custom-code all of our websites in-house. We don’t have any requirements as to what tools you use for your design, but we ask that you follow these guidelines.
IMAGES:
If you use any images or icons in the design, we ask that you have a link to the asset so we can purchase the image/icon. Most of the designs we submit do not have the customer’s images on them unless they have some great images. Be creative; show us the feeling you are trying to portray with your image choices. Use any royalty-free site you choose. We subscribe to Adobe and mainly use their images, but we can purchase images outside of Adobe. PLEASE NOTE: we will not submit designs to clients with watermarks on the images.
FONTS:
We ask that you identify the fonts you’re using in the design. This can be done in a message if you want. We typically use Google Fonts and Adobe Fonts.
CONTENT:
We're always open to different content and ideas. We often submit designs with stock images so the client can see our vision. We typically take pictures after the website launch to use their images with our vision. Lorem Ipsum is fine for paragraphs, but we ask that you make the Headers with correct English. We want to be able to show the vision and identify the sections of the website.
INSPIRATION:
We typically add a couple of links in the brief of websites we like to help you get started in your design.
REVISIONS:
We do not often ask for revisions of the designs unless we see something in the design that may not appeal to the client. If there are slight changes that we want to make, we do that in the development process.
FEEDBACK:
We rarely give feedback on designs during the design process. We are working on many website projects and do not have the time to provide feedback. We usually respond if your request is well thought out and asks specific questions, but a note asking “feedback, please” usually goes unanswered.

```html
<!DOCTYPE html>
<html lang="en">
<head>
<meta charset="utf-8">
<title>Lumen Womens Shelter</title>
<link rel="stylesheet" href="https://fonts.googleapis.com/css2?family=Poppins:wght@300;400;500;600;700&display=swap">
<style>
:root{
  --purple:#4a1d84;
  --purple-deep:#3b1670;
  --coral:#f76a55;
  --green:#3ab54a;
  --gray:#eeeeee;
  --ink:#222222;
  --muted:#555555;
  --white:#ffffff;
}
*{margin:0;padding:0;box-sizing:border-box}
html,body{width:1200px;height:5046px;overflow:hidden}
body{font-family:'Poppins',sans-serif;color:var(--ink);background:var(--white);position:relative}
.abs{position:absolute}
.pill{position:absolute;border-radius:40px;display:flex;align-items:center;justify-content:center;color:var(--white);font-weight:500;text-transform:uppercase;z-index:2}
.purple{background:var(--purple)}
.coral{background:var(--coral)}
.photo{position:absolute}
.rule{position:absolute;height:4px;width:56px}
.rule::before{content:"";position:absolute;left:0;top:0;width:12px;height:4px;background:var(--green);border-radius:2px}
.rule::after{content:"";position:absolute;left:18px;top:0;width:38px;height:4px;background:var(--green);border-radius:2px}
.heading{font-weight:500;font-size:40px;color:var(--ink)}

/* header */
.brand{left:88px;top:40px;display:flex;align-items:center;gap:12px}
.brand-mark{width:36px;height:36px;border-radius:50%;background:var(--purple)}
.brand-name{font-size:34px;font-weight:600;color:var(--purple);letter-spacing:-1px}
.brand-sub{left:140px;top:92px;font-size:8px;letter-spacing:2px;color:var(--purple)}
.nav{left:546px;top:78px;display:flex;gap:27px;font-size:14px;color:var(--ink)}

/* hero */
.hero-photo{left:570px;top:130px;width:630px;height:635px;background:linear-gradient(90deg,#ffffff 0%,#e6d3cd 30%,#c9a58f 60%,#8a6a5a 100%)}
.hero-title{left:88px;top:236px;font-size:47px;font-weight:600;line-height:58px;color:var(--ink)}
.hero-sub{left:92px;top:436px;font-size:18.5px;line-height:25px;color:var(--ink)}
.hotline-btn{left:88px;top:540px;width:344px;height:90px;flex-direction:column;text-transform:none;font-size:22px;line-height:28px}
.hotline-btn b{font-weight:600;font-size:18px}
.exit-btn{left:950px;top:732px;width:176px;height:68px;font-size:16px;border:2px solid #e14c3a;gap:14px;z-index:10}

/* mission */
.mission-band{left:0;top:765px;width:1200px;height:955px;background:var(--gray)}
.mission-photo{left:150px;top:815px;width:420px;height:745px;border-radius:0 260px 0 260px;background:linear-gradient(160deg,#c7d3d1,#a88a4c 55%,#6d5a4a)}
.mission-text{left:617px;top:1106px;width:508px;font-size:14.5px;line-height:26px;color:var(--muted)}
.btn-md{height:64px;font-size:15px}

/* values */
.value{position:absolute;width:172px;height:172px;border-radius:50%;background:var(--white);display:flex;align-items:center;justify-content:center;z-index:2}
.value-inner{width:148px;height:148px;border-radius:50%;background:var(--purple);border:2px dashed rgba(255,255,255,.6);outline:4px solid var(--purple);outline-offset:-6px;display:flex;flex-direction:column;align-items:center;justify-content:center;color:var(--white);font-weight:600;font-size:17px;text-align:center;line-height:20px;gap:6px}

/* services */
.service{position:absolute;top:1910px;width:322px;height:410px;border:2px solid #dddddd;border-radius:26px;text-align:center}
.service-photo{position:absolute;left:8px;top:8px;width:302px;height:202px}
.service h3{position:absolute;left:20px;right:20px;top:244px;font-size:14.5px;font-weight:500;color:var(--purple);line-height:18px}
.service p{position:absolute;left:42px;right:42px;font-size:13.5px;line-height:19px;color:var(--ink);text-align:justify;text-align-last:center}

/* hotline */
.hotline-band{left:0;top:2570px;width:1200px;height:930px;background:var(--gray)}
.hotline-box{left:212px;top:2482px;width:758px;height:248px;background:var(--purple);border-radius:30px;color:var(--white);text-align:center;z-index:2}
.hotline-box .t1{position:absolute;left:0;right:0;top:50px;font-size:60px;font-weight:700}
.hotline-box .t2{position:absolute;left:0;right:0;top:125px;font-size:64px;font-weight:500;letter-spacing:2px}
.deco-dot{left:160px;top:2400px;width:70px;height:70px;border-radius:50%;background:linear-gradient(135deg,#f76a55,#4a1d84)}

/* blog */
.blog-photo{left:0;top:2840px;width:556px;height:512px;border-radius:0 40px 40px 0;background:linear-gradient(120deg,#c08a5a,#e2c7a4 50%,#7d8d93)}
.blog-title{left:629px;top:2982px;width:500px;font-size:42px;font-weight:300;line-height:50px;color:var(--ink)}
.blog-meta{left:631px;top:3164px;display:flex;gap:22px;font-size:11px;color:var(--ink);align-items:center}
.blog-meta span{display:flex;align-items:center;gap:6px}
.blog-text{left:629px;top:3202px;width:490px;font-size:14.5px;line-height:26px;color:var(--muted)}
.btn-sm{height:48px;font-size:14px}

/* events */
.events-intro{left:0;width:1200px;top:3702px;text-align:center;font-size:14.5px;line-height:26px;color:var(--muted)}
.event-photo{position:absolute;top:3808px;width:316px;height:200px}
.event-card{position:absolute;top:3915px;width:250px;height:200px;background:#f7f6fb;padding:32px 34px}
.event-card .date{font-size:11px;color:var(--ink)}
.event-card h4{font-size:18px;font-weight:500;margin-top:10px}
.event-card p{font-size:11.5px;line-height:18px;margin-top:10px;color:var(--ink)}
.event-card a{display:block;margin-top:14px;font-size:13px;font-style:italic;color:var(--purple);text-decoration:underline}

/* contact */
.contact-band{left:0;top:4318px;width:1200px;height:597px;background:linear-gradient(90deg,var(--purple) 0%,var(--purple) 45%,#6a3f8f 70%,#8d5e8e 100%)}
.field{position:absolute;height:42px;border-radius:22px;background:var(--white);display:flex;align-items:center;padding-left:20px;gap:8px;font-size:14.5px;color:#888888}
.field svg{flex:none}

/* footer */
.footer{left:0;top:4915px;width:1200px;height:131px;background:var(--coral);color:var(--white)}
.footer .copy{position:absolute;left:103px;top:62px;font-size:14px}
.footer .social{position:absolute;left:476px;top:56px;display:flex;gap:8px}
.footer .social span{width:32px;height:32px;border-radius:50%;border:2px solid var(--white)}
.footer .links{position:absolute;left:688px;top:60px;font-size:14px;font-weight:500}
</style>
</head>
<body>

<!-- Header -->
<div class="abs brand"><span class="brand-mark"></span><span class="brand-name">Lumen</span></div>
<div class="abs brand-sub">WOMENS SHELTER</div>
<div class="pill purple" style="left:760px;top:16px;width:110px;height:44px;font-size:13px">Donate</div>
<div class="pill purple" style="left:876px;top:16px;width:112px;height:44px;font-size:13px">Get Help</div>
<div class="pill coral" style="left:996px;top:16px;width:120px;height:44px;font-size:13px">Volunteer</div>
<nav class="abs nav"><span>Home</span><span>Our Mission</span><span>Get Involved</span><span>Programs</span><span>Blog</span><span>Contact us</span></nav>

<!-- Hero -->
<div class="photo hero-photo" role="img" aria-label="Photo of a young woman and her mother smiling together"></div>
<h1 class="abs hero-title">Creating A World<br>Without<br>Domestic Violence</h1>
<p class="abs hero-sub">Provide services and shelter for women and<br>mothers throughout California</p>
<div class="pill purple hotline-btn"><span>Call our hotline at</span><b>xxx-xxx-xxxx | 000-000-0000</b></div>

<!-- Mission -->
<div class="abs mission-band"></div>
<div class="pill coral exit-btn"><span>x</span><span>Exit Now</span></div>
<div class="photo mission-photo" role="img" aria-label="Photo of teenagers studying together at a table"></div>
<h2 class="abs heading" style="left:617px;top:972px">Our Mission</h2>
<div class="rule" style="left:620px;top:1036px"></div>
<p class="abs mission-text">Lorem ipsum dolor sit amet, consectetur adipiscing elit, sed do eiusmod tempor incididunt ut labore et dolore magna aliqua. Ut enim ad minim veniam, quis nostrud exercitation ullamco laboris nisi ut aliquip ex ea commodo consequat. Duis aute irure dolor in reprehenderit in voluptate velit esse cillum dolore eu fugiat nulla pariatur. Excepteur sint occaecat cupidatat non proident, sunt in culpa qui officia deserunt mollit anim id est laborum.</p>
<div class="pill purple btn-md" style="left:617px;top:1332px;width:174px">Know More</div>
<div class="pill coral btn-md" style="left:805px;top:1332px;width:176px">Donate</div>

<!-- Values -->
<div class="value" style="left:269px;top:1630px"><div class="value-inner">
  <svg width="46" height="50" viewBox="0 0 46 50"><path d="M23 2 L42 9 V24 C42 36 33 44 23 48 C13 44 4 36 4 24 V9 Z" fill="#fff"/><path d="M14 25 L21 32 L33 18" stroke="#4a1d84" stroke-width="5" fill="none" stroke-linecap="round" stroke-linejoin="round"/></svg>
  SAFETY</div></div>
<div class="value" style="left:519px;top:1630px"><div class="value-inner">
  <svg width="50" height="44" viewBox="0 0 50 44"><path d="M25 42 C8 30 2 22 2 13 C2 6 8 1 14 1 C19 1 23 4 25 8 C27 4 31 1 36 1 C42 1 48 6 48 13 C48 22 42 30 25 42 Z" fill="#fff"/></svg>
  RESPECT</div></div>
<div class="value" style="left:761px;top:1630px"><div class="value-inner">
  <svg width="48" height="40" viewBox="0 0 48 40"><g stroke="#fff" stroke-width="3" fill="none"><path d="M24 2 V36 M12 38 H36 M6 8 H42"/><path d="M6 8 L0 22 H12 Z M42 8 L36 22 H48 Z" fill="#fff"/></g></svg>
  SOCIAL<br>JUSTICE</div></div>

<!-- Services -->
<div class="service" style="left:88px">
  <div class="service-photo" role="img" aria-label="Photo of a woman helping an elderly woman with a phone" style="background:linear-gradient(135deg,#8fa36d,#c9b9a8 50%,#6b7a5a)"></div>
  <h3>DOMESTIC VIOLENCE SERVICES</h3>
  <p style="top:282px">Lorem ipsum dolor sit amet, consef ghctetur adipiscing elit, sed do eiu smod tempor inci didunt ut abore et dolore</p>
</div>
<div class="service" style="left:443px">
  <div class="service-photo" role="img" aria-label="Photo of a mother comforting her upset teenage son" style="background:linear-gradient(135deg,#6f8f8a,#c6a486 55%,#e0d1c0)"></div>
  <h3>HOMELESS AND FAMILY<br>SUPPORT SERVICES</h3>
  <p style="top:300px">Lorem ipsum dolor sit amet, consef ghctetur adipiscing elit, sed do eiu smod tempor inci</p>
</div>
<div class="service" style="left:796px">
  <div class="service-photo" role="img" aria-label="Photo of two women hugging on a couch" style="background:linear-gradient(135deg,#d9cfc4,#a98f7e 50%,#eae6e2)"></div>
  <h3>SEXUAL ASSAULT SERVICES</h3>
  <p style="top:282px">Lorem ipsum dolor sit amet, consef ghctetur adipiscing elit, sed do eiu smod tempor inci didunt ut abore et dolore</p>
</div>

<!-- Hotline -->
<div class="abs hotline-band"></div>
<div class="abs deco-dot"></div>
<div class="abs hotline-box"><div class="t1">24 HOUR HOTLINE</div><div class="t2">XXX.XXX.XXXX</div></div>

<!-- Blog -->
<div class="photo blog-photo" role="img" aria-label="Photo of young women laughing together outdoors"></div>
<h2 class="abs heading" style="left:629px;top:2866px">Blog</h2>
<div class="rule" style="left:631px;top:2934px"></div>
<h3 class="abs blog-title">Why You Matter in the Fight Against Domestic Violence</h3>
<div class="abs blog-meta">
  <span><svg width="11" height="11" viewBox="0 0 11 11"><rect x="0.5" y="1.5" width="10" height="9" fill="none" stroke="#333"/><rect x="0.5" y="1.5" width="10" height="3" fill="#333"/></svg>FEB 20, 2023</span>
  <span><svg width="11" height="11" viewBox="0 0 11 11"><circle cx="5.5" cy="3" r="2.6" fill="#333"/><path d="M0.5 11 C1 6.5 10 6.5 10.5 11 Z" fill="#333"/></svg>MarenHolloway</span>
</div>
<p class="abs blog-text">Lorem ipsum dolor sit amet, consectetur adipiscing elit, sed do eiusmod tempor incididunt ut labore et dolore magna aliqua. Ut</p>
<div class="pill purple btn-sm" style="left:629px;top:3290px;width:140px">Read More</div>
<div class="pill coral btn-sm" style="left:785px;top:3290px;width:142px">View All Blog</div>

<!-- Events -->
<h2 class="abs heading" style="left:0;width:1200px;text-align:center;top:3596px">Upcoming Events</h2>
<div class="rule" style="left:572px;top:3664px"></div>
<p class="abs events-intro">Lorem ipsum dolor sit amet, consectetur adipiscing elit. Maecenas ornare<br>nulla ut dui euismod pretium. Sed varius sagittis lacus, a tincidunt dui</p>

<div class="event-photo" role="img" aria-label="Photo of a mother and young daughter" style="left:90px;background:linear-gradient(135deg,#9b8f86,#d8c7bb 60%,#eee6e0)"></div>
<div class="event-card" style="left:90px"><div class="date">JAN 25, 2023</div><h4>Post 1 Headline</h4><p>Lorem ipsum dolor sit amet, consectetur adipi</p><a>Read More</a></div>
<div class="event-photo" role="img" aria-label="Photo of a smiling mother hugging her child" style="left:447px;background:linear-gradient(135deg,#6a5f58,#b69a86 55%,#4e4845)"></div>
<div class="event-card" style="left:447px"><div class="date">JAN 25, 2023</div><h4>Post 2 Headline</h4><p>Lorem ipsum dolor sit amet, consectetur adipi</p><a>Read More</a></div>
<div class="event-photo" role="img" aria-label="Photo of a family playing together at home" style="left:802px;background:linear-gradient(135deg,#3f5a55,#c5c1bd 55%,#7a6d66)"></div>
<div class="event-card" style="left:802px"><div class="date">JAN 25, 2023</div><h4>Post 3 Headline</h4><p>Lorem ipsum dolor sit amet, consectetur adipi</p><a>Read More</a></div>

<div class="pill purple" style="left:526px;top:4178px;width:148px;height:58px;font-size:14px">View All</div>

<!-- Contact -->
<div class="abs contact-band" role="img" aria-label="Purple tinted photo of smiling women together"></div>
<h2 class="abs heading" style="left:96px;top:4398px;color:#fff">Contact Us</h2>
<div class="rule" style="left:98px;top:4466px"></div>
<div class="field" style="left:96px;top:4546px;width:254px"><svg width="12" height="12" viewBox="0 0 12 12"><circle cx="6" cy="3.5" r="3" fill="#4a1d84"/><path d="M0.5 12 C1 7 11 7 11.5 12 Z" fill="#4a1d84"/></svg>Your Name</div>
<div class="field" style="left:366px;top:4546px;width:254px"><svg width="12" height="12" viewBox="0 0 12 12"><path d="M2 1 L4.5 1 L5.5 4 L4 5 C5 7 6 8 7.5 8.5 L8.5 7 L11 8 L11 10.5 C6 11 1 6 2 1 Z" fill="#4a1d84"/></svg>Phone Number</div>
<div class="field" style="left:96px;top:4616px;width:254px"><svg width="12" height="10" viewBox="0 0 12 10"><rect width="12" height="10" rx="1" fill="#4a1d84"/><path d="M1 1.5 L6 5.5 L11 1.5" stroke="#fff" fill="none"/></svg>Email Address</div>
<div class="field" style="left:366px;top:4616px;width:258px"><svg width="12" height="14" viewBox="0 0 12 14"><path d="M6 14 C2 9 0.5 7 0.5 5 A5.5 5.5 0 0 1 11.5 5 C11.5 7 10 9 6 14 Z" fill="#4a1d84"/><circle cx="6" cy="5" r="2" fill="#fff"/></svg>Address</div>
<div class="field" style="left:96px;top:4683px;width:528px;height:82px;border-radius:30px;align-items:flex-start;padding-top:28px"><svg width="12" height="12" viewBox="0 0 12 12"><circle cx="6" cy="6" r="6" fill="#4a1d84"/><circle cx="3.5" cy="6" r="1" fill="#fff"/><circle cx="6" cy="6" r="1" fill="#fff"/><circle cx="8.5" cy="6" r="1" fill="#fff"/></svg>Message</div>
<div class="pill coral" style="left:278px;top:4800px;width:134px;height:48px;font-size:15px">Submit</div>

<!-- Footer -->
<footer class="abs footer">
  <div class="copy">Copyright @ 2023 All rights reserved</div>
  <div class="social"><span></span><span></span><span></span><span></span></div>
  <div class="links">Our Mission | Get Involved &nbsp;| Programs| Blog | Contact us</div>
</footer>

</body>
</html>
```